a mobile app for beauty salon professional to publish their service and customers to book service

I plan to create an iPhone app (support iPhone 6 and above) that will allow beauty salon professionals (e.g. hair stylist) to publish their service/business with address/geolocation and available time slots, manage their professional profile with photos, and service charges, allow the customers to search services based on locations, and book the service. customer can provide feedback/ratings on the professional's service. a reference website : http://velmo.trimbook.example/booking/

Target Market(s)

beauty and hair salon professionals and customers

Industry/Entity Type

Hair And Beauty

Font styles to use
Sans Serif
Script

Colors

Designer to choose colors to be used in the design.

Requirements
Must have
• === customer features
• - user/customer registration
• - customer browse nearby service using a map view
• - customer browse nearby service using a list view ordered by distance (e.g. km)
• - customer search salon service based on service category, price range, and profressional's rating
• - customer select a service with zoom in details : salon name, service offered, location/address, and a "booking" button
• - customer place booking by specifying service (e.g. simple cut, blow-dry, etc) required, time slot, preferred professional
• - customer payments (paypal/credit card)
• - customer can feedback/rate on the salon professional
• === salon professional features
• - user/professional registration
• - maintain professional profile (private/public), option to upload photos
• - a registered professional can register/maintain shop/business who by default is the owner of the shop/business
• - a shop owner can assign professionals to the shop/business (multiple professional can work in the same location/shop)
• - professional maintain their service and schedule (breaks, holidays, working hours, appointments, service rates)

```html
<!DOCTYPE html>
<html lang="en">
<head>
<meta charset="utf-8">
<title>Beauty Salon App Design</title>
<link rel="stylesheet" href="https://fonts.googleapis.com/css2?family=Poppins:wght@500;600;700&family=Roboto:wght@400;500&display=swap">
<style>
:root{
  --bg:#232327;
  --purple:#9452b1;
  --purple-dark:#7d3d9b;
  --pink:#e8418c;
  --pink-soft:#f7c9de;
  --ink:#1f1f24;
  --muted:#6d6d75;
  --line:#e3e3e8;
  --white:#ffffff;
  --yellow:#f5c40f;
  --cyan:#19c6d6;
  --blue:#2f7bf0;
  --lime:#b6ea1b;
  --magenta:#c520d6;
  --red:#ee2a55;
}
*{box-sizing:border-box;margin:0;padding:0}
html,body{width:1200px;height:1200px;overflow:hidden;background:var(--bg)}
body{font-family:'Roboto',sans-serif;color:var(--ink)}
.stage{position:absolute;left:0;top:0;width:1500px;height:1500px;transform:scale(.8);transform-origin:0 0;background:var(--bg)}
.abs{position:absolute}
.headline{position:absolute;left:0;width:1430px;text-align:center;font-family:'Poppins',sans-serif;font-weight:700}
.headline-main{top:66px;font-size:70px;color:var(--purple);letter-spacing:-1px}
.headline-sub{top:158px;font-size:42px;font-weight:500;color:var(--pink)}
.deco{position:absolute}
.screen{position:absolute;width:330px;height:586px;background:var(--white);overflow:hidden}
.status{position:absolute;left:0;top:0;width:330px;height:18px;font-size:11px;color:var(--ink)}
.status .carrier{position:absolute;left:6px;top:3px}
.status .time{position:absolute;left:0;width:330px;text-align:center;top:3px;font-weight:500}
.status .batt{position:absolute;right:8px;top:3px}
.status .batt i{display:inline-block;width:20px;height:8px;background:currentColor;border-radius:1px;margin-left:3px;vertical-align:-1px}
.on-purple .status{color:var(--white)}
.appbar{position:absolute;left:0;top:0;width:330px;height:56px;background:var(--purple)}
.appbar-title{position:absolute;top:28px;left:0;width:330px;text-align:center;color:var(--white);font-size:16px;font-family:'Poppins',sans-serif;font-weight:500}
.back{position:absolute;left:12px;top:28px}
/* splash */
.brand{position:absolute;left:0;top:210px;width:330px;text-align:center;color:var(--pink);font-family:'Poppins',sans-serif;font-weight:500}
.brand-name{font-size:44px;line-height:1}
.brand-sub{font-size:20px;letter-spacing:2px;margin-top:6px}
.brand-dot{width:14px;height:14px;border-radius:50%;background:var(--purple);margin:18px auto 0}
/* create account */
.page-title{position:absolute;top:28px;left:0;width:330px;text-align:center;color:var(--purple);font-size:15px;font-family:'Poppins',sans-serif;font-weight:500}
.social{position:absolute;left:30px;width:268px;height:38px;border-radius:19px;border:1.5px solid;font-size:15px;display:flex;align-items:center;padding-left:50px}
.social .mark{position:absolute;left:16px;top:11px;width:14px;height:14px;border-radius:50%}
.social-a{top:88px;border-color:#3b5bb5;color:#3b5bb5}
.social-a .mark{background:#3b5bb5}
.social-b{top:145px;border-color:var(--red);color:var(--red)}
.social-b .mark{background:var(--red)}
.or-line{position:absolute;top:217px;left:0;width:330px;text-align:center;font-size:11px;color:var(--muted)}
.field{position:absolute;left:30px;width:268px;height:40px;border-bottom:1px solid var(--line);font-size:14px;color:var(--muted);padding-left:36px;line-height:40px}
.field svg{position:absolute;left:2px;top:12px}
.terms{position:absolute;top:444px;left:0;width:330px;text-align:center;font-size:12.5px;line-height:18px;color:var(--ink)}
.terms span{color:var(--pink)}
.btn-primary{position:absolute;height:38px;border-radius:19px;background:var(--purple);color:var(--white);font-size:15px;font-weight:500;text-align:center;line-height:38px}
/* map */
.search-pill{position:absolute;left:42px;top:20px;width:246px;height:30px;border-radius:15px;background:#f1f1f4;text-align:center;line-height:30px;font-size:15px}
.filter{position:absolute;right:10px;top:27px}
.result-count{position:absolute;top:60px;left:0;width:330px;text-align:center;font-size:11.5px;color:var(--pink)}
.map-area{position:absolute;left:0;top:78px;width:330px;height:470px;background:linear-gradient(160deg,#f1eee6 0%,#e9e6dd 35%,#cfe3f3 48%,#e9e6dd 60%,#f3f0e8 100%)}
.sheet{position:absolute;left:0;top:538px;width:330px;height:48px;background:var(--white);border-radius:12px 12px 0 0;box-shadow:0 -2px 8px rgba(0,0,0,.08);text-align:center;color:var(--purple);font-size:12px;font-weight:500;padding-top:26px}
.sheet svg{position:absolute;left:158px;top:9px}
/* list */
.list-bar{position:absolute;left:0;top:0;width:330px;height:56px;background:var(--purple)}
.list-pill{position:absolute;left:42px;top:20px;width:246px;height:30px;border-radius:15px;background:var(--purple-dark);color:var(--white);text-align:center;line-height:30px;font-size:15px}
.list-bg{position:absolute;left:0;top:56px;width:330px;height:530px;background:#f0f0f3}
.salon{position:absolute;left:0;width:330px;height:116px;background:var(--white)}
.salon .photo{position:absolute;left:12px;top:14px;width:62px;height:62px;border-radius:50%;background:radial-gradient(circle at 40% 40%,#a9825b,#4a3323)}
.salon .name{position:absolute;left:87px;top:12px;font-size:15px;font-weight:500}
.salon .dist{position:absolute;right:8px;top:15px;font-size:11px;color:var(--muted)}
.salon .addr{position:absolute;left:87px;top:33px;font-size:13px;color:#333}
.salon .svc{position:absolute;left:87px;top:57px;font-size:11px;color:var(--muted);padding-left:22px}
.salon .svc svg{position:absolute;left:0;top:0}
.salon .book{position:absolute;left:12px;width:306px;top:86px;border-top:1px solid var(--line);text-align:center;padding-top:6px;font-size:13px;color:var(--pink);font-weight:500}
/* booking */
.step-title{position:absolute;left:12px;top:67px;font-size:19px;font-family:'Poppins',sans-serif;font-weight:500}
.step-count{position:absolute;right:12px;top:74px;font-size:12.5px;color:#333}
.steps{position:absolute;left:0;top:97px;width:330px;height:40px}
.label{position:absolute;left:12px;font-size:11px;color:#333}
.input{position:absolute;left:12px;width:305px;height:46px;background:var(--white);box-shadow:0 1px 5px rgba(0,0,0,.14);border-radius:2px;font-size:15px;line-height:46px;padding-left:13px}
.input svg{position:absolute}
.avatar{position:absolute;right:30px;top:7px;width:32px;height:32px;border-radius:50%;background:radial-gradient(circle at 50% 40%,#7b7f86,#3a3d42)}
.nav{position:absolute;top:538px;font-size:13px;color:var(--purple);font-weight:500}
.nav-circle{position:absolute;top:538px;width:36px;height:36px;border-radius:50%;background:var(--purple)}
.month{position:absolute;top:150px;left:0;width:310px;text-align:center;font-size:15px}
.days{position:absolute;left:8px;top:183px;width:314px;display:flex}
.days div{flex:1;text-align:center;font-size:9.5px;color:#555}
.days div b{display:block;font-weight:400;font-size:15px;color:#333;margin:8px auto 0;width:30px;height:30px;line-height:30px;border-radius:50%}
.days div.sel{color:var(--pink)}
.days div.sel b{background:var(--purple);color:var(--white);font-weight:500}
.divider{position:absolute;left:0;top:240px;width:330px;height:1px;background:var(--line)}
.slot{position:absolute;width:71px;height:32px;border:1px solid #f3c7da;border-radius:4px;color:var(--pink);text-align:center;line-height:30px;font-size:15px}
.slot.sel{background:var(--pink);border-color:var(--pink);color:var(--white)}
.card{position:absolute;left:12px;top:190px;width:305px;height:162px;background:var(--white);box-shadow:0 1px 5px rgba(0,0,0,.12)}
.row{position:absolute;left:0;width:305px;height:40px;border-bottom:1px solid var(--line);font-size:13px;color:var(--muted);padding-left:46px;line-height:40px}
.row:last-child{border-bottom:none}
.row svg{position:absolute;left:14px;top:11px}
.notes{position:absolute;left:26px;top:382px;font-size:13px;color:var(--muted);padding-left:33px;line-height:20px}
.notes svg{position:absolute;left:0;top:1px}
.done-title{position:absolute;top:347px;left:0;width:330px;text-align:center;font-size:19px;font-weight:500}
.done-text{position:absolute;top:386px;left:0;width:330px;text-align:center;font-size:14.5px;line-height:18px;color:#333}
.done-thanks{position:absolute;top:441px;left:0;width:330px;text-align:center;font-size:14.5px}
</style>
</head>
<body>
<div class="stage">

  <h1 class="headline headline-main">Beauty Salon</h1>
  <p class="headline headline-sub">App Design</p>

  <svg class="deco" style="left:380px;top:30px" width="760" height="170" viewBox="0 0 760 170">
    <circle cx="17" cy="50" r="11" fill="none" stroke="var(--magenta)" stroke-width="5"/>
    <path d="M178 5v16M170 13h16" stroke="var(--lime)" stroke-width="5"/>
    <path d="M685 43v20M675 53h20" stroke="var(--cyan)" stroke-width="6"/>
    <circle cx="136" cy="153" r="8" fill="none" stroke="var(--yellow)" stroke-width="5"/>
    <circle cx="553" cy="153" r="10" fill="none" stroke="var(--red)" stroke-width="5"/>
    <path d="M648 142v16M640 150h16" stroke="var(--blue)" stroke-width="5"/>
    <circle cx="727" cy="142" r="8" fill="none" stroke="var(--yellow)" stroke-width="5"/>
  </svg>

  <!-- Splash -->
  <section class="screen" style="left:56px;top:252px">
    <div class="brand">
      <div class="brand-name">velmo's</div>
      <div class="brand-sub">SALOON</div>
      <div class="brand-dot"></div>
    </div>
  </section>

  <!-- Create account -->
  <section class="screen" style="left:409px;top:252px">
    <div class="status"><span class="carrier">▮▮▮ Nexa</span><span class="time">9:41 AM</span><span class="batt">100%<i></i></span></div>
    <svg class="back" style="top:29px" width="12" height="18" viewBox="0 0 12 18"><path d="M9 2L2 9l7 7" fill="none" stroke="var(--purple)" stroke-width="2"/></svg>
    <div class="page-title">Create New Account</div>
    <div class="social social-a"><span class="mark"></span>Continue with Linkora</div>
    <div class="social social-b"><span class="mark"></span>Continue with Searchly</div>
    <div class="or-line">OR SIGN UP USING EMAIL</div>
    <div class="field" style="top:258px"><svg width="18" height="18" viewBox="0 0 18 18"><circle cx="9" cy="6" r="4" fill="none" stroke="#666" stroke-width="1.3"/><path d="M2 17c0-4 3-6 7-6s7 2 7 6z" fill="none" stroke="#666" stroke-width="1.3"/></svg>full name</div>
    <div class="field" style="top:297px"><svg width="18" height="18" viewBox="0 0 18 18"><rect x="1" y="4" width="16" height="11" fill="none" stroke="#666" stroke-width="1.3"/><path d="M1 4l8 6 8-6" fill="none" stroke="#666" stroke-width="1.3"/></svg>email address</div>
    <div class="field" style="top:337px;border-bottom:none"><svg width="18" height="18" viewBox="0 0 18 18"><rect x="3" y="8" width="12" height="9" fill="none" stroke="#666" stroke-width="1.3"/><path d="M5.5 8V5a3.5 3.5 0 017 0v3" fill="none" stroke="#666" stroke-width="1.3"/></svg>password
      <svg style="left:246px;top:14px" width="20" height="12" viewBox="0 0 20 12"><path d="M1 6c3-6 15-6 18 0-3 6-15 6-18 0z" fill="none" stroke="var(--pink)" stroke-width="1.2"/><circle cx="10" cy="6" r="2.5" fill="none" stroke="var(--pink)" stroke-width="1.2"/></svg>
    </div>
    <p class="terms">By creating an account, you agree to our<br><span>Terms of Service</span> &amp; <span>Privacy Policy</span></p>
    <div class="btn-primary" style="left:44px;top:512px;width:242px">Register</div>
  </section>

  <!-- Map view -->
  <section class="screen" style="left:761px;top:252px">
    <div class="status"><span class="carrier">▮▮▮ Nexa</span><span class="time">9:41 AM</span><span class="batt">100%<i></i></span></div>
    <svg class="back" style="top:29px" width="12" height="18" viewBox="0 0 12 18"><path d="M9 2L2 9l7 7" fill="none" stroke="var(--purple)" stroke-width="2"/></svg>
    <div class="search-pill">haircut for men</div>
    <svg class="filter" width="20" height="16" viewBox="0 0 20 16"><path d="M1 2h18M4 7h12M7 12h6" stroke="var(--purple)" stroke-width="2"/></svg>
    <div class="result-count">Showing 280 salons in Harbourview</div>
    <div class="map-area" role="img" aria-label="City street map with pink pins marking nearby salons and the user's location"></div>
    <div class="sheet"><svg width="14" height="12" viewBox="0 0 14 12"><path d="M2 6l5-4 5 4M2 11l5-4 5 4" fill="none" stroke="var(--purple)" stroke-width="1.4"/></svg>Show All Lists</div>
  </section>

  <!-- List view -->
  <section class="screen on-purple" style="left:1114px;top:252px">
    <div class="list-bar"></div>
    <div class="status"><span class="carrier">▮▮▮ Nexa</span><span class="time">9:41 AM</span><span class="batt">100%<i></i></span></div>
    <svg class="back" style="top:29px" width="12" height="18" viewBox="0 0 12 18"><path d="M9 2L2 9l7 7" fill="none" stroke="#fff" stroke-width="2"/></svg>
    <div class="list-pill">haircut for men</div>
    <svg class="filter" width="20" height="16" viewBox="0 0 20 16"><path d="M1 2h18M4 7h12M7 12h6" stroke="#fff" stroke-width="2"/></svg>
    <div class="list-bg"></div>

    <div class="salon" style="top:56px"><div class="photo" role="img" aria-label="Salon interior photo"></div><div class="name">Orchid Salon and Spa</div><div class="dist">0.6 km</div><div class="addr">412 W 9th Ave, Harbourview, BC</div><div class="svc"><svg width="14" height="12" viewBox="0 0 14 12"><rect x="1" y="1" width="12" height="10" rx="1" fill="none" stroke="#888"/><path d="M1 5h12" stroke="#888"/></svg>Blowdry &amp; Style, Simple Cut, Style Cut</div><div class="book">BOOK</div></div>
    <div class="salon" style="top:180px"><div class="photo" role="img" aria-label="Salon interior photo"></div><div class="name">Mirela's Beauty Care</div><div class="dist">0.8 km</div><div class="addr">1870 Cedar St, Harbourview, BC</div><div class="svc"><svg width="14" height="12" viewBox="0 0 14 12"><rect x="1" y="1" width="12" height="10" rx="1" fill="none" stroke="#888"/><path d="M1 5h12" stroke="#888"/></svg>Blowdry &amp; Style, Simple Cut, Nails</div><div class="book">BOOK</div></div>
    <div class="salon" style="top:305px"><div class="photo" role="img" aria-label="Salon interior photo" style="background:radial-gradient(circle at 40% 40%,#c9c6cf,#5d5866)"></div><div class="name">Lumi Beauty Salon</div><div class="dist">1 km</div><div class="addr">96 E Harbour Rd, Harbourview, BC</div><div class="svc"><svg width="14" height="12" viewBox="0 0 14 12"><rect x="1" y="1" width="12" height="10" rx="1" fill="none" stroke="#888"/><path d="M1 5h12" stroke="#888"/></svg>Blowdry &amp; Style, Simple Cut, Style Cut</div><div class="book">BOOK</div></div>
    <div class="salon" style="top:429px"><div class="photo" role="img" aria-label="Salon interior photo"></div><div class="name">Orchid Salon and Spa</div><div class="dist">0.6 km</div><div class="addr">412 W 9th Ave, Harbourview, BC</div><div class="svc"><svg width="14" height="12" viewBox="0 0 14 12"><rect x="1" y="1" width="12" height="10" rx="1" fill="none" stroke="#888"/><path d="M1 5h12" stroke="#888"/></svg>Blowdry &amp; Style, Simple Cut, Style Cut</div><div class="book">BOOK</div></div>
    <div class="salon" style="top:553px"><div class="photo" role="img" aria-label="Salon interior photo"></div><div class="name">Mirela's Beauty Care</div><div class="dist">0.8 km</div></div>
  </section>

  <!-- Step icons reused per screen -->
  <!-- Booking step 1 -->
  <section class="screen on-purple" style="left:56px;top:861px">
    <div class="appbar"></div>
    <div class="status"><span class="carrier">▮▮▮ Nexa</span><span class="time">9:41 AM</span><span class="batt">100%<i></i></span></div>
    <svg class="back" width="12" height="18" viewBox="0 0 12 18"><path d="M9 2L2 9l7 7" fill="none" stroke="#fff" stroke-width="2"/></svg>
    <div class="appbar-title">Booking</div>
    <div class="step-title">Services</div><div class="step-count">STEP 1 OF 4</div>
    <svg class="steps" viewBox="0 0 330 40" width="330" height="40">
      <g stroke="var(--purple)" stroke-width="1.2" fill="none"><path d="M64 20h38M146 20h38M228 20h38"/></g>
      <circle cx="41" cy="20" r="18" fill="var(--pink)"/>
      <g stroke="#fff" stroke-width="1.4" fill="none"><circle cx="41" cy="16" r="4"/><path d="M33 24c4 4 12 4 16 0"/></g>
      <g stroke="var(--purple)" stroke-width="1.4" fill="none"><circle cx="124" cy="20" r="8"/><path d="M124 15v5l3 3"/><path d="M206 17v9"/><circle cx="206" cy="13" r=".8" fill="var(--purple)"/><path d="M281 21l5 5 10-11"/></g>
    </svg>
    <div class="label" style="top:168px">SELECT SERVICE</div>
    <div class="input" style="top:190px">Blowdry &amp; Style<svg style="right:14px;top:20px" width="10" height="7" viewBox="0 0 10 7"><path d="M1 1l4 4 4-4" fill="none" stroke="var(--pink)" stroke-width="1.4"/></svg></div>
    <div class="label" style="top:265px">ON OR AFTER</div>
    <div class="input" style="top:287px">13 March 2018<svg style="right:13px;top:15px" width="17" height="16" viewBox="0 0 17 16"><rect x="1" y="2" width="15" height="13" rx="1" fill="none" stroke="var(--pink)" stroke-width="1.1"/><path d="M4 7h2M8 7h2M12 7h2M4 11h2M8 11h2M12 11h2" stroke="var(--pink)"/></svg></div>
    <div class="label" style="top:362px">WITH</div>
    <div class="input" style="top:384px">Daniel Reyes<span class="avatar" role="img" aria-label="Stylist profile photo"></span><svg style="right:14px;top:20px" width="10" height="7" viewBox="0 0 10 7"><path d="M1 1l4 4 4-4" fill="none" stroke="var(--pink)" stroke-width="1.4"/></svg></div>
    <div class="nav" style="right:60px;top:549px">NEXT</div>
    <div class="nav-circle" style="left:281px"><svg width="36" height="36" viewBox="0 0 36 36"><path d="M11 18h14M19 12l6 6-6 6" fill="none" stroke="#fff" stroke-width="2"/></svg></div>
  </section>

  <!-- Booking step 2 -->
  <section class="screen on-purple" style="left:409px;top:861px">
    <div class="appbar"></div>
    <div class="status"><span class="carrier">▮▮▮ Nexa</span><span class="time">9:41 AM</span><span class="batt">100%<i></i></span></div>
    <svg class="back" width="12" height="18" viewBox="0 0 12 18"><path d="M9 2L2 9l7 7" fill="none" stroke="#fff" stroke-width="2"/></svg>
    <div class="appbar-title">Booking</div>
    <div class="step-title">Time</div><div class="step-count">STEP 2 OF 4</div>
    <svg class="steps" viewBox="0 0 330 40" width="330" height="40">
      <g stroke="var(--purple)" stroke-width="1.2" fill="none"><path d="M64 20h38M146 20h38M228 20h38"/></g>
      <circle cx="124" cy="20" r="18" fill="var(--pink)"/>
      <g stroke="var(--pink)" stroke-width="1.4" fill="none"><circle cx="41" cy="16" r="4"/><path d="M33 24c4 4 12 4 16 0"/></g>
      <g stroke="#fff" stroke-width="1.4" fill="none"><circle cx="124" cy="20" r="8"/><path d="M124 15v5l3 3"/></g>
      <g stroke="var(--purple)" stroke-width="1.4" fill="none"><path d="M206 17v9"/><circle cx="206" cy="13" r=".8" fill="var(--purple)"/><path d="M281 21l5 5 10-11"/></g>
    </svg>
    <div class="month">March 2018</div>
    <div class="days">
      <div>Tue<b>13</b></div><div>Wed<b>14</b></div><div>Thu<b>15</b></div><div class="sel">Fri<b>16</b></div><div>Sat<b>17</b></div><div>Sun<b>18</b></div><div>Mon<b>19</b></div>
    </div>
    <div class="divider"></div>
    <div class="slot" style="left:9px;top:254px">8:00</div><div class="slot" style="left:89px;top:254px">8:30</div><div class="slot" style="left:170px;top:254px">9:00</div><div class="slot" style="left:250px;top:254px">9:30</div>
    <div class="slot" style="left:9px;top:298px">10:00</div><div class="slot" style="left:89px;top:298px">10:30</div><div class="slot" style="left:170px;top:298px">11:00</div><div class="slot" style="left:250px;top:298px">13:00</div>
    <div class="slot" style="left:9px;top:342px">13:30</div><div class="slot sel" style="left:89px;top:342px">14:00</div><div class="slot" style="left:170px;top:342px">14:30</div><div class="slot" style="left:250px;top:342px">15:00</div>
    <div class="slot" style="left:9px;top:386px">15:30</div><div class="slot" style="left:89px;top:386px">16:00</div><div class="slot" style="left:170px;top:386px">16:30</div>
    <div class="nav-circle" style="left:13px"><svg width="36" height="36" viewBox="0 0 36 36"><path d="M25 18H11M17 12l-6 6 6 6" fill="none" stroke="#fff" stroke-width="2"/></svg></div>
    <div class="nav" style="left:60px;top:549px">BACK</div>
    <div class="nav" style="right:60px;top:549px">NEXT</div>
    <div class="nav-circle" style="left:281px"><svg width="36" height="36" viewBox="0 0 36 36"><path d="M11 18h14M19 12l6 6-6 6" fill="none" stroke="#fff" stroke-width="2"/></svg></div>
  </section>

  <!-- Booking step 3 -->
  <section class="screen on-purple" style="left:761px;top:861px">
    <div class="appbar"></div>
    <div class="status"><span class="carrier">▮▮▮ Nexa</span><span class="time">9:41 AM</span><span class="batt">100%<i></i></span></div>
    <svg class="back" width="12" height="18" viewBox="0 0 12 18"><path d="M9 2L2 9l7 7" fill="none" stroke="#fff" stroke-width="2"/></svg>
    <div class="appbar-title">Booking</div>
    <div class="step-title">Details</div><div class="step-count">STEP 3 OF 4</div>
    <svg class="steps" viewBox="0 0 330 40" width="330" height="40">
      <g stroke="var(--purple)" stroke-width="1.2" fill="none"><path d="M64 20h38M146 20h38M228 20h38"/></g>
      <circle cx="206" cy="20" r="18" fill="var(--pink)"/>
      <g stroke="var(--pink)" stroke-width="1.4" fill="none"><circle cx="41" cy="16" r="4"/><path d="M33 24c4 4 12 4 16 0"/><circle cx="124" cy="20" r="8"/><path d="M124 15v5l3 3"/></g>
      <g stroke="#fff" stroke-width="1.6" fill="none"><path d="M206 17v9"/><circle cx="206" cy="13" r=".8" fill="#fff"/></g>
      <path d="M281 21l5 5 10-11" stroke="var(--purple)" stroke-width="1.4" fill="none"/>
    </svg>
    <div class="label" style="top:168px">ACCOUNT</div>
    <div class="card">
      <div class="row" style="top:0"><svg width="18" height="18" viewBox="0 0 18 18"><circle cx="9" cy="6" r="4" fill="none" stroke="#666" stroke-width="1.3"/><path d="M2 17c0-4 3-6 7-6s7 2 7 6z" fill="none" stroke="#666" stroke-width="1.3"/></svg>First name</div>
      <div class="row" style="top:40px"><svg width="18" height="18" viewBox="0 0 18 18"><circle cx="9" cy="6" r="4" fill="none" stroke="#666" stroke-width="1.3"/><path d="M2 17c0-4 3-6 7-6s7 2 7 6z" fill="none" stroke="#666" stroke-width="1.3"/></svg>Last name</div>
      <div class="row" style="top:80px"><svg width="18" height="18" viewBox="0 0 18 18"><rect x="1" y="4" width="16" height="11" fill="none" stroke="#666" stroke-width="1.3"/><path d="M1 4l8 6 8-6" fill="none" stroke="#666" stroke-width="1.3"/></svg>Email address</div>
      <div class="row" style="top:120px;border-bottom:none"><svg width="18" height="18" viewBox="0 0 18 18"><path d="M3 2l3 0 2 4-2 2c1 2 2 3 4 4l2-2 4 2v3c-7 1-14-6-13-13z" fill="none" stroke="#666" stroke-width="1.2"/></svg>Phone number</div>
    </div>
    <div class="notes"><svg width="18" height="18" viewBox="0 0 18 18"><rect x="3" y="1" width="13" height="15" fill="none" stroke="#666" stroke-width="1.2"/><path d="M6 5h7M6 8h7M6 11h4" stroke="#666"/></svg>Add Notes</div>
    <div class="nav-circle" style="left:13px"><svg width="36" height="36" viewBox="0 0 36 36"><path d="M25 18H11M17 12l-6 6 6 6" fill="none" stroke="#fff" stroke-width="2"/></svg></div>
    <div class="nav" style="left:60px;top:549px">BACK</div>
    <div class="nav" style="right:60px;top:549px">NEXT</div>
    <div class="nav-circle" style="left:281px"><svg width="36" height="36" viewBox="0 0 36 36"><path d="M11 18h14M19 12l6 6-6 6" fill="none" stroke="#fff" stroke-width="2"/></svg></div>
  </section>

  <!-- Booking step 4 -->
  <section class="screen on-purple" style="left:1114px;top:861px">
    <div class="appbar"></div>
    <div class="status"><span class="carrier">▮▮▮ Nexa</span><span class="time">9:41 AM</span><span class="batt">100%<i></i></span></div>
    <svg class="back" width="12" height="18" viewBox="0 0 12 18"><path d="M9 2L2 9l7 7" fill="none" stroke="#fff" stroke-width="2"/></svg>
    <div class="appbar-title">Booking</div>
    <div class="step-title">Done</div><div class="step-count">STEP 4 OF 4</div>
    <svg class="steps" viewBox="0 0 330 40" width="330" height="40">
      <g stroke="var(--purple)" stroke-width="1.2" fill="none"><path d="M64 20h38M146 20h38M228 20h38"/></g>
      <circle cx="289" cy="20" r="18" fill="var(--pink)"/>
      <g stroke="var(--pink)" stroke-width="1.4" fill="none"><circle cx="41" cy="16" r="4"/><path d="M33 24c4 4 12 4 16 0"/><circle cx="124" cy="20" r="8"/><path d="M124 15v5l3 3"/><path d="M206 17v9"/><circle cx="206" cy="13" r=".8" fill="var(--pink)"/></g>
      <path d="M281 21l5 5 10-11" stroke="#fff" stroke-width="1.8" fill="none"/>
    </svg>
    <svg class="abs" style="left:94px;top:179px" width="142" height="142" viewBox="0 0 142 142">
      <defs><linearGradient id="doneGrad" x1="0" y1="0" x2="1" y2="1"><stop offset="0" stop-color="#f0509c"/><stop offset="1" stop-color="#d81f7a"/></linearGradient></defs>
      <circle cx="71" cy="71" r="70" fill="#fbe1ed"/>
      <circle cx="71" cy="71" r="56" fill="#f4b2d1"/>
      <circle cx="71" cy="71" r="44" fill="url(#doneGrad)"/>
      <g fill="none" stroke="#fff" stroke-width="2.2"><rect x="52" y="54" width="38" height="34" rx="4"/><path d="M52 64h38M61 49v9M81 49v9"/><rect x="58" y="69" width="6" height="5"/><rect x="68" y="69" width="6" height="5"/><rect x="78" y="69" width="6" height="5"/><rect x="58" y="78" width="6" height="5"/><rect x="68" y="78" width="6" height="5"/><path d="M78 81l3 3 5-5"/></g>
    </svg>
    <div class="done-title">Booking Successful</div>
    <p class="done-text">Your booking has been<br>successfully received.</p>
    <p class="done-thanks">Thank you!</p>
    <div class="btn-primary" style="left:13px;top:534px;width:304px">Done</div>
  </section>

</div>
</body>
</html>
```